Wine label - premium, elegant & classic

We are a young husband and wife team who have worked in the wine industry for 10+ years. This year we've finally had the opportunity to make our own wine and release our own brand. Our wines are boutique and sell at a mid-premium price (we don't make a lot) so we're looking for a label design that can reflect this premium nature and mixes traditional design elements with modern reflections.

The brand is called: M&L
Updates

Project Deadline Extended
Reason: We've received some great design concepts over the past week which we would happily pay for, so we've decided to guarantee payment and extend the deadline to allow time for more designs to be sent through. A BIG thanks to all who have already submitted, your designs are still under consideration. Cheers, L.

A big thank you to all for taking the time to submit your beautiful designs to our project.  We now have the very tough job of looking over each of them and selecting only one.  We hope to come to a decision in the next day or two, so hopefully we won't keep you waiting too long!

Cheers, and thanks again

M&L.                                   

Target Market(s)

30 - 45 year old female and male wine drinkers

Industry/Entity Type

Industry

Requirements
Must have
• Can we please see two versions of the one design - one for a red wine and one for a white wine.

The front labels needs to include the following information:
1. Brand name: M&L
2. Wine varieties: Pinot Noir (red wine) and Sauvignon Blanc (white wine)
3. Vintage: 2012 for both
4. Region: Yarra Valley
5. GI: Wine of Australia (not essential to be on front label)

The back label needs to include the following:
1. The brand name: M&L
2. Variety, vintage, region and volume (the volume must be 4mm in height)
3. Room for product description - approx. 30-40 words.
4. Alcohol statement (no size restriction, pls use 12.5% ALC/VOL as example)
5. Standard drinks (no size restriction, pls use 'Approx.7.8 standard drinks' as example)
6. Sulphites statement: "Sulphites added."
7. Allergen statement: "Fined with the aid of egg and milk products and traces may remain."
8. Room for address: Approx. 20 words
9. "Wine of Australia" - no size restriction, just needs to be legible

Packaging presentation:
Pinot Noir is a red wine and Sauvignon Blanc is a white wine.
Labels for both need to be shown on premium punted burgundy bottles (pls see example: http://www.pelvornglass.com/products_services/pvg_premium_burgundy_750_ml_wine_bottle.html)
Nice to have
• We would like the design to embody the following elements:
1. Classically modern
2. Clean and simple
3. Elegance
4. Restricted use of colours (ideally just black/grey, white/buff and perhaps one other)

Some design examples of what we like:
1. http://www.fenwickhollow.com.au/sangiovese-tasting-notes/
2. http://corlunbend.com/Wines/Corlun-Bend-Vineyard/Range/2010-Corlun-Bend-Single-Vineyard-Pinot-Noir-.htm
Should not have
• Preferrably won't have any photos or drawings unless you feel there is a simple symbol or image that could be used to enhance the design.

Restricted use of colours - more muted, conservative tones.

```html
<!DOCTYPE html>
<html lang="en">
<head>
<meta charset="utf-8">
<title>M&amp;L — Yarra Valley 2012 labels</title>
<link href="https://fonts.googleapis.com/css2?family=Crimson+Pro:wght@400;500;600;700&display=swap" rel="stylesheet">
<style>
  :root {
    --canvas: #ffffff;
    --paper: #f7f7f5;
    --ink: #111111;
    --label-black: #141414;
    --band-dark: #3a3a3a;
    --band-light: #c9c9c9;
    --muted: #8a8a8a;
    --muted-dark: #a8a8a8;
    --white: #ffffff;
  }
  html, body {
    margin: 0;
    padding: 0;
    width: 1200px;
    height: 900px;
    overflow: hidden;
    background: var(--canvas);
  }
  .range {
    position: relative;
    width: 1200px;
    height: 900px;
    font-family: "Crimson Pro", Georgia, serif;
  }
  .label {
    position: absolute;
    top: 235px;
    width: 410px;
    height: 430px;
    box-sizing: border-box;
    overflow: hidden;
  }
  .label--white {
    left: 150px;
    background: var(--paper);
    border: 1px solid #e2e2de;
    color: var(--ink);
  }
  .label--red {
    left: 640px;
    background: var(--label-black);
    color: var(--white);
  }
  .label__brand {
    position: absolute;
    top: 52px;
    left: 0;
    right: 0;
    margin: 0;
    text-align: center;
    font-size: 104px;
    font-weight: 500;
    line-height: 1;
    letter-spacing: -0.01em;
  }
  .label__band {
    position: absolute;
    top: 220px;
    height: 27px;
    display: flex;
    align-items: center;
    justify-content: center;
    font-size: 16px;
    font-weight: 600;
    letter-spacing: 0.2em;
    text-transform: uppercase;
  }
  .label--white .label__band {
    left: 0;
    right: 22px;
    background: var(--band-dark);
    color: var(--white);
  }
  .label--red .label__band {
    left: 22px;
    right: 0;
    background: var(--band-light);
    color: var(--ink);
  }
  .label__region {
    position: absolute;
    top: 302px;
    left: 0;
    right: 0;
    text-align: center;
    font-size: 15px;
    letter-spacing: 0.28em;
    text-transform: uppercase;
  }
  .label--white .label__region { color: var(--muted); }
  .label--red .label__region { color: var(--muted-dark); }
  .label__vintage {
    position: absolute;
    top: 342px;
    left: 0;
    right: 0;
    text-align: center;
    font-size: 15px;
    font-weight: 700;
    letter-spacing: 0.55em;
    padding-left: 0.55em;
  }
</style>
</head>
<body>
  <main class="range">
    <section class="label label--white" aria-label="Sauvignon Blanc front label">
      <h1 class="label__brand">M&amp;L</h1>
      <div class="label__band">Sauvignon Blanc</div>
      <div class="label__region">Yarra Valley</div>
      <div class="label__vintage">2012</div>
    </section>

    <section class="label label--red" aria-label="Pinot Grigio front label">
      <h2 class="label__brand">M&amp;L</h2>
      <div class="label__band">Pinot Grigio</div>
      <div class="label__region">Yarra Valley</div>
      <div class="label__vintage">2012</div>
    </section>
  </main>
</body>
</html>
```